New Fresh design for online Rabbit Game

Hi,

we are a french company working on a online rabbits game for kids, and not kids.

Our website is www.trovelu.fr, but you can look at the US version : www.hoplark.com

We buy our actual design 2 years ago, but we now think it's too boring and washed out...

We need yours talent to make a really more exacting, more colorful, fresh and dynamic design.

In our game, players have to breed and train rabbits and to make them run races. Players run again friends or players.

Players are kids, between 8 and 15 years. But best players are often parents of these kids !

Our ambiance is clearly funny. We really like if color theme or background look like a nice blue sky, and / or beach. Something that make people happy to come, and say "You are here on holly days to have fun !"

I think the best is if we have 2 layouts, one for the Home page, and one for all other page.

For home page, we are really open to any proposition, we just need to keep our features :
- registration (with rabbit preview)
- connection
- game preview (images slide with small text)
- live race preview (as we have actually)

For other pages layout, we need a layout with a standard container (maybe 850 px width?), and our 2 navigation's bar.

We only need psd, no html integration.

Thanks for your help, please ask me for any questions.
Updates

Hi, 

I have just added some information, concerning layout.

Also we have just committed the budget.

Target Market(s)

Mostly kids between 8 and 15 years.

Industry/Entity Type

It Company

Requirements
Must have
• We already have some characters, like Mr Pebblo at the home page and our rabbits. We want to keep all of them, so new design have to match with there style (carton).

If you create an account, you will see we have a big nav bar with 6 tabs, and a little top bar. We absolutely need them to keep a easy navigation in website.

We also need some proposition of element style, like h1, h2, h3, hr, inputs, buttons, notification bubble, etc... So we can work to improve all our pages.
Nice to have
• I think the actual website is a little to wide (about 1000px width). Maybe something like 900px - 850px is more elegant ?
In this case, we can arrange pages to deal with it.

It can be cool if major colors are stil blue and green, to match a little with actual colors. But it's no very important.
Should not have
• We don't want too big header picture (for the all pages layout). I mean, players have to focus on the content.

We don't want photo realistic style, our style is cartoon.

We don't want flash. But Js animations are ok.

```html
<!DOCTYPE html>
<html lang="en">
<head>
<meta charset="utf-8">
<title>Hoplark – Racing and Breeding Game</title>
<link href="https://fonts.googleapis.com/css2?family=Fredoka:wght@500;600&family=Gabriela&family=Gudea:wght@400;700&display=swap" rel="stylesheet">
<style>
:root{
  --sky-top:#1f8fd6;
  --sky-mid:#49b3ec;
  --sky-low:#9fd9f5;
  --sea:#5fc3e0;
  --sand:#f1dfb0;
  --topbar:#133a5c;
  --navy:#0f3a66;
  --heading-blue:#1a4f9c;
  --heading-green:#5f8f1c;
  --orange:#f26a1b;
  --orange-dark:#d9480f;
  --red:#d6301c;
  --yellow:#f9c21b;
  --lime:#9ad622;
  --lime-dark:#5ea10f;
  --ink:#1b1b1b;
  --footer:#142c47;
  --footer-link:#f1f1f1;
  --footer-accent:#f3c31a;
}
*{box-sizing:border-box;margin:0;padding:0}
html,body{width:1200px;height:930px;overflow:hidden}
body{font-family:"Gudea",Arial,sans-serif;color:var(--ink);
  background:linear-gradient(180deg,var(--sky-top) 0,var(--sky-mid) 35%,var(--sky-low) 62%,var(--sea) 78%,var(--sand) 92%);}
.stage{position:relative;width:1200px;height:930px}
.scenery{position:absolute;inset:19px 0 72px 0;
  background:radial-gradient(ellipse 260px 180px at 90px 560px,#ffffff 0,rgba(255,255,255,.85) 60%,rgba(255,255,255,0) 100%),
             radial-gradient(ellipse 160px 420px at 1140px 700px,#2f7a2a 0,rgba(47,122,42,.6) 55%,rgba(47,122,42,0) 100%);}

/* top bar */
.topbar{position:absolute;top:0;left:0;width:1200px;height:19px;background:var(--topbar);
  color:#fff;font-size:11px;display:flex;align-items:center;padding-left:207px;white-space:nowrap}
.topbar a{color:#fff;text-decoration:none;margin-right:14px;display:flex;align-items:center;gap:4px}
.topbar .dot{width:9px;height:9px;border-radius:2px;display:inline-block}
.topbar .greet{margin-right:14px}
.topbar .right{position:absolute;right:200px;display:flex;gap:14px}

/* header */
.brand{position:absolute;left:202px;top:40px;display:flex;align-items:center;gap:16px}
.brand-mark{width:62px;height:62px;border-radius:50%;background:#fff}
.brand-name{font-family:"Fredoka",sans-serif;font-weight:600;font-size:40px;color:var(--orange)}
.chef{position:absolute;left:650px;top:26px;width:118px;height:128px;border-radius:50% 50% 40% 40%;
  background:radial-gradient(circle at 50% 45%,#4a4f8c,#2d2d55 70%,#5b3c22 100%);z-index:3}

.mainnav{position:absolute;left:202px;top:119px;width:568px;height:36px;
  background:linear-gradient(180deg,#c9f06a,var(--lime) 60%,var(--lime-dark));border-radius:6px 0 0 0;
  display:flex;align-items:stretch;padding-left:9px;z-index:2}
.mainnav a{font-size:15px;color:#1d2a05;text-decoration:none;padding:0 9px;display:flex;align-items:center;white-space:nowrap}
.mainnav a.active{background:linear-gradient(180deg,#ffb23a,var(--orange));color:#fff}

.login{position:absolute;left:773px;top:34px;width:226px;height:122px;background:linear-gradient(180deg,#2e78d1,#1c57a8);
  border-radius:8px 8px 4px 4px;color:#fff;padding:6px 10px;z-index:2}
.login h3{font-family:"Gabriela",serif;font-weight:400;font-size:17px;display:flex;align-items:center;gap:10px;margin:0 0 8px 2px}
.login h3 .lock{width:18px;height:18px;border-radius:3px;background:var(--yellow)}
.login .row{display:flex;align-items:center;justify-content:space-between;font-size:13px;margin-bottom:5px;white-space:nowrap}
.login input{width:134px;height:19px;border:1px solid #9fd0f5;background:#fff}
.login .foot{display:flex;justify-content:space-between;align-items:center;margin-top:7px}
.login .forgot{font-size:10px;color:#fff;text-decoration:underline;white-space:nowrap}

.btn{font-family:"Fredoka",sans-serif;font-weight:600;color:#102a00;border:1px solid var(--lime-dark);
  background:linear-gradient(180deg,#d7fb7e,var(--lime) 55%,var(--lime-dark));border-radius:5px;
  display:flex;align-items:center;justify-content:center;white-space:nowrap}
.btn-sm{width:72px;height:22px;font-size:14px}

/* panel */
.panel{position:absolute;left:207px;top:155px;width:787px;height:688px;
  background:linear-gradient(180deg,rgba(255,255,255,.95),rgba(239,249,244,.93));box-shadow:0 0 6px rgba(0,0,0,.25)}
.panel > *{position:absolute}
.tagline{left:10px;top:12px;width:767px;height:27px;background:#fff;font-family:"Fredoka",sans-serif;font-weight:500;
  font-size:18px;display:flex;align-items:center;padding-left:6px;white-space:nowrap}
.h-script{font-family:"Gabriela",serif;font-weight:400;font-size:23px;color:var(--heading-blue);white-space:nowrap}
.h-script .green{color:var(--heading-green)}

.overview-title{left:12px;top:40px;font-size:24px}
.tabs{left:12px;top:86px;width:374px;height:26px;display:flex;background:linear-gradient(180deg,#ff7a2a,var(--orange-dark))}
.tabs span{color:#fff;font-family:"Fredoka",sans-serif;font-weight:500;font-size:13px;display:flex;align-items:center;justify-content:center;white-space:nowrap}
.tabs .tab-pen{width:83px}
.tabs .tab-allot{width:123px}
.tabs .tab-prof{width:82px}
.tabs .tab-univ{width:86px}
.tabs span.active{background:linear-gradient(180deg,#ffd64d,#f3a418);color:#222}
.slide{left:12px;top:124px;width:373px;height:174px;border:4px solid #fff;box-shadow:0 0 4px rgba(0,0,0,.35);
  background:linear-gradient(135deg,#36c6d0,#4bb8a8 40%,#6b5aa8 70%,#2e2e52)}
.slide .caption{position:absolute;left:0;right:0;bottom:0;background:rgba(0,0,0,.6);color:#fff;font-size:12.5px;padding:3px 6px;line-height:1.15}
.slide .caption b{font-weight:700}
.thumbs{left:12px;top:314px;display:flex;gap:7px}
.thumbs span{width:88px;height:56px;border:2px solid #222}
.thumbs .t1{background:linear-gradient(135deg,#3fc2c8,#4b4a80)}
.thumbs .t2{background:linear-gradient(135deg,#6b5a2e,#3d5a25)}
.thumbs .t3{background:linear-gradient(135deg,#e8d06a,#4b6aa8)}
.thumbs .t4{background:linear-gradient(180deg,#dff4ff,#68c43a)}

.player-title{left:431px;top:40px}
.register-note{left:431px;top:84px;font-family:"Fredoka",sans-serif;font-weight:500;color:var(--red);font-size:15.5px;white-space:nowrap}
.step{left:431px;height:28px;display:flex;align-items:center;gap:14px;font-family:"Fredoka",sans-serif;font-weight:500;color:var(--navy);font-size:15px;white-space:nowrap}
.step .num{width:28px;height:28px;border-radius:50%;background:radial-gradient(circle at 40% 35%,#ff6a3a,#c81e0c);color:#fff;
  display:flex;align-items:center;justify-content:center;font-size:14px;line-height:1;box-shadow:0 0 0 2px #fff;flex:none}
.step1{top:119px}.step2{top:229px}.step3{top:303px}
.name-field{left:612px;top:124px;width:160px;height:23px;background:linear-gradient(90deg,#f6a81a,var(--yellow));
  display:flex;align-items:center;justify-content:space-between;padding:0 4px 0 12px;font-family:"Fredoka",sans-serif;font-weight:500;font-size:14px}
.name-field .edit{color:#fff;font-size:13px;display:flex;align-items:center;gap:6px}
.name-field .edit i{width:17px;height:17px;background:#cfe6ff;border:1px solid #6a9ad6;display:inline-block}
.bunny-preview{left:431px;top:155px;width:60px;height:62px;border-radius:40% 50% 30% 30%;background:linear-gradient(180deg,#ece3cf,#c9bca1)}
.option{left:506px;width:103px;height:22px;display:flex;align-items:center;justify-content:space-between;
  font-family:"Fredoka",sans-serif;font-weight:500;color:var(--heading-green);font-size:15px;white-space:nowrap}
.opt1{top:152px}.opt2{top:178px}.opt3{top:205px}
.username{left:470px;top:266px;width:158px;height:23px;border:1px solid var(--lime-dark);background:#fff;font-size:11px;color:#777;padding-left:7px;display:flex;align-items:center}
.play-big{left:472px;top:341px;width:88px;height:28px;font-size:17px}
.smith{left:648px;top:175px;width:126px;height:156px;border-radius:45% 45% 30% 30%;background:linear-gradient(180deg,#6e6448,#3a3428 60%,#2a2a2a)}

.divider{left:12px;top:389px;width:765px;border:0;border-top:1px dashed #b9c4bb}
.welcome-title{left:12px;top:398px;font-size:26px}
.quote{left:12px;top:448px;width:226px;font-size:13px;line-height:15px}
.quote .mark{color:var(--red);font-family:"Gabriela",serif;font-size:28px;line-height:.5;display:block;height:12px}
.quote b{font-weight:700}
.signature{left:12px;top:597px;font-family:"Fredoka",sans-serif;font-weight:500;color:var(--red);font-size:13px;white-space:nowrap}
.continue{left:13px;top:641px;width:88px;height:28px;font-size:15px}
.turtle{left:227px;top:455px;width:160px;height:215px;border-radius:50% 50% 40% 40%;background:radial-gradient(circle at 45% 45%,#9cc43a,#4e7a1c 65%,#7a5a2a)}

.race-title{left:402px;top:404px;font-family:"Gabriela",serif;font-size:22px;color:var(--navy);white-space:nowrap}
.race-title .green{color:var(--heading-green)}
.race{left:400px;top:450px;width:372px;height:219px;border:4px solid #fff;box-shadow:0 0 4px rgba(0,0,0,.35);
  background:linear-gradient(180deg,#b07a3c 0,#b07a3c 18%,#8a8f9a 20%,#aab0ba 45%,#a8642c 47%,#b3723a 100%)}

/* footer */
.footer{position:absolute;left:0;top:858px;width:1200px;height:72px;background:var(--footer);color:var(--footer-link);font-size:12px}
.footer a{color:inherit;text-decoration:none}
.footer .links{position:absolute;left:207px;top:17px;display:flex;gap:12px;white-space:nowrap}
.footer .copy{position:absolute;left:207px;top:46px;font-size:11.5px;white-space:nowrap}
.footer .partners{position:absolute;left:857px;top:18px;color:var(--footer-accent);font-size:11.5px;display:flex;align-items:center;gap:6px}
.footer .badge{width:78px;height:27px;background:#1f5a9a;border:1px solid #7fb3e8;border-radius:3px}
.footer .site{position:absolute;left:857px;top:46px;font-size:11.5px}
.footer .site span{color:var(--footer-accent)}
</style>
</head>
<body>
<div class="stage">
  <div class="scenery" role="img" aria-label="Cartoon beach scene with clouds, sea, sand and palm trees"></div>

  <div class="topbar">
    <span class="greet">Hi, Guest !</span>
    <a href="#"><i class="dot" style="background:#f5c518;border-radius:50%"></i>Coins</a>
    <a href="#"><i class="dot" style="background:#e0283a"></i>Ruby</a>
    <a href="#"><i class="dot" style="background:#f2c94c"></i>Message</a>
    <a href="#"><i class="dot" style="background:#46b22d"></i>Notification</a>
    <a href="#"><i class="dot" style="background:#5aa8e6;border-radius:50%"></i>Forum</a>
    <a href="#"><i class="dot" style="background:#f5c518"></i>Rankings</a>
    <a href="#"><i class="dot" style="background:#8f7ad6;border-radius:50%"></i>Account</a>
    <div class="right"><span>4:57am</span><a href="#"><i class="dot" style="background:#cfe3f7"></i>Signup</a></div>
  </div>

  <div class="brand"><span class="brand-mark"></span><span class="brand-name">Hoplark</span></div>
  <div class="chef" role="img" aria-label="Cartoon chef character holding a spoon over a tray of vegetables"></div>

  <nav class="mainnav">
    <a class="active" href="#">Home</a><a href="#">Pen</a><a href="#">Allotment</a><a href="#">Races</a>
    <a href="#">Profession</a><a href="#">Market</a><a href="#">Lapin</a>
  </nav>

  <form class="login">
    <h3><span class="lock"></span>Connexion</h3>
    <div class="row"><label>Uesename :</label><input type="text"></div>
    <div class="row"><label>Password :</label><input type="password"></div>
    <div class="foot"><a class="forgot" href="#">Forgotten your password?</a><span class="btn btn-sm">Play</span></div>
  </form>

  <main class="panel">
    <div class="tagline">The Coolest Racing and Breeding Game There is ....</div>

    <h2 class="h-script overview-title">Game Overview !</h2>
    <div class="tabs"><span class="tab-pen">Your Pen</span><span class="tab-allot">Your Allotment</span><span class="tab-prof active">Professions</span><span class="tab-univ">Universe</span></div>
    <div class="slide" role="img" aria-label="Cartoon professions characters: blacksmith, alchemist, gardener and scientist">
      <div class="caption"><b>Blacksmith, Alchemist, Gardner or Scientist!</b> Progress in a profession and learn how to make really powerful objects!</div>
    </div>
    <div class="thumbs">
      <span class="t1" role="img" aria-label="Professions preview"></span>
      <span class="t2" role="img" aria-label="Allotment preview"></span>
      <span class="t3" role="img" aria-label="Universe preview"></span>
      <span class="t4" role="img" aria-label="Pen preview"></span>
    </div>

    <h2 class="h-script player-title">New Player ?</h2>
    <p class="register-note">Register in just a couple of seconds !</p>
    <div class="step step1"><span class="num">1</span>Choose Your Bunny</div>
    <div class="name-field">Ange<span class="edit">Edit<i></i></span></div>
    <div class="bunny-preview" role="img" aria-label="Preview of the chosen bunny"></div>
    <div class="option opt1"><svg width="16" height="14"><path d="M0 7 8 0v4h8v6H8v4z" fill="#2f7fe0"/></svg>Original<svg width="16" height="14"><path d="M16 7 8 0v4H0v6h8v4z" fill="#2f7fe0"/></svg></div>
    <div class="option opt2"><svg width="16" height="14"><path d="M0 7 8 0v4h8v6H8v4z" fill="#2f7fe0"/></svg>Yellow<svg width="16" height="14"><path d="M16 7 8 0v4H0v6h8v4z" fill="#2f7fe0"/></svg></div>
    <div class="option opt3"><svg width="16" height="14"><path d="M0 7 8 0v4h8v6H8v4z" fill="#2f7fe0"/></svg>Male<svg width="16" height="14"><path d="M16 7 8 0v4H0v6h8v4z" fill="#2f7fe0"/></svg></div>
    <div class="step step2"><span class="num">2</span>Choose A Username</div>
    <div class="username">Username</div>
    <div class="step step3"><span class="num">3</span>OK ! We're Good To Go!</div>
    <span class="btn play-big">Play</span>
    <div class="smith" role="img" aria-label="Cartoon blacksmith character holding a hammer"></div>

    <hr class="divider">

    <h2 class="h-script welcome-title">Welcome <span class="green">to Hoplark!</span></h2>
    <p class="quote"><span class="mark">&ldquo;</span>&nbsp;&nbsp;&nbsp;&nbsp;Ready to become a bunny breeder? Hi, I'm <b>Mr Pebblo!</b> I'm going to explain the rules of the game. It'll only take 5 minutes, and then I'll give you some gifts to help you start out. Follow the guide!</p>
    <p class="signature">Mr Pebblo !</p>
    <span class="btn continue">Continue</span>
    <div class="turtle" role="img" aria-label="Cartoon guide character giving a thumbs up"></div>

    <h2 class="race-title">Take part in races <span class="green">with other players</span></h2>
    <div class="race" role="img" aria-label="Live race preview with bunnies running on a dirt track in front of spectators"></div>
  </main>

  <footer class="footer">
    <div class="links"><a href="#">Rules</a><span>-</span><a href="#">General Terms and Conditions</a><span>-</span><a href="#">Contact</a></div>
    <div class="copy">Copyright © Hoplark 2012-13.All Right Reserved</div>
    <div class="partners">Partners :<span class="badge"></span></div>
    <div class="site"><span>Trovelu.fr</span> - view all</div>
  </footer>
</div>
</body>
</html>
```